Homes, Invest in Non-performing loans

We need only 3 web pages, one for the home, one for the content, one for the properties.
The main focus of our business is to offer non performing loans (before foreclosures) to the general public. All the non-performing mortgages will end in a house, an apartment, a store, etc.
Our customers are able to invest from 10,000usd to 1,000,000usd (average 50,000usd).
Our customers' usual focus groups are employees who want second earnings, perceiving the business feeling without outlay time. They look for a solid finance sense corporation that confers them certainty.
Nearly all our clients desire the house, apartment, store, etc. more than the actual earnings.
The name of our company is BRAMLEX
Reason: We value the time and effort you already invest in our project. We realize that we did't come back on some of the doubts requested by the designers. It will be inequitable to the designers who prerequisite our feedback. We also appreciate the comprehension of the community in this postponement.
Reason: Designers,
We really apreciate all the time and effort you put on our project. From the begining we ask for 3 pages, so now we will leave the 10 finalist and provide some extra time to submit the other 2 pages.
We will race the price in 10%
Target Market(s)
Our customers average investors works as employees and want to have a second income or business without spending time. (People from 35 to 50)
Industry/Entity Type
Finance
Requirements
Should not have
- FLASH

```html
<!DOCTYPE html>
<html lang="en">
<head>
<meta charset="utf-8">
<title>Bramlex – Home</title>
<link rel="stylesheet" href="https://fonts.googleapis.com/css2?family=Ubuntu:ital,wght@0,400;0,500;0,700;1,500&family=Yanone+Kaffeesatz:wght@300;400;700&display=swap">
<style>
:root{
  --page-bg:#ebebeb;
  --panel:#ffffff;
  --panel-border:#dcdcdc;
  --olive:#7f7a24;
  --olive-light:#8f8a2e;
  --olive-dark:#5f5b18;
  --heading-olive:#5d5a16;
  --charcoal:#3d3d3d;
  --charcoal-dark:#2b2b2b;
  --text:#3a3a3a;
  --muted:#555;
  --white:#fff;
}
*{box-sizing:border-box;margin:0;padding:0}
html,body{width:1200px;height:1011px;overflow:hidden}
body{background:var(--page-bg);font-family:"Ubuntu",sans-serif;color:var(--text);position:relative}
a{color:inherit;text-decoration:none}

/* header */
.brand{position:absolute;left:123px;top:56px;font-family:"Ubuntu",sans-serif;font-weight:700;font-size:34px;color:var(--charcoal-dark);letter-spacing:1px;display:flex;align-items:center;gap:10px}
.brand-mark{width:22px;height:22px;background:var(--olive)}
.call{position:absolute;right:173px;top:19px;font-size:11px;color:var(--muted);display:flex;align-items:baseline;gap:9px}
.call strong{font-weight:400;font-size:16px;color:#222;letter-spacing:.5px}
.social{position:absolute;left:1038px;top:19px;display:flex;gap:4px}
.social span{width:20px;height:20px;border-radius:3px;display:block}
.social .s1{background:#4a78bf}.social .s2{background:#1d84b5}
.news{position:absolute;left:764px;top:64px;font-size:11px;color:var(--olive-dark);text-decoration:underline;font-weight:500}
.search{position:absolute;left:888px;top:59px;display:flex;height:26px}
.search input{width:145px;border:1px solid #ddd;border-right:0;border-radius:3px 0 0 3px;background:#f7f7f7;font:italic 9px "Ubuntu",sans-serif;padding-left:9px;color:#aaa}
.search button{width:57px;border:0;border-radius:0 3px 3px 0;background:linear-gradient(#5a5a5a,#2e2e2e);color:#fff;font:14px "Ubuntu",sans-serif}
.nav{position:absolute;left:601px;top:105px;width:489px;height:41px;display:flex;border-radius:3px;overflow:hidden;box-shadow:0 1px 2px rgba(0,0,0,.3)}
.nav a{flex:1;display:flex;align-items:center;justify-content:center;font-family:"Yanone Kaffeesatz",sans-serif;font-size:22px;font-weight:300;color:#fff;background:linear-gradient(var(--olive-light),var(--olive-dark));border-left:1px solid #a6a14a}
.nav a.current{background:linear-gradient(#666,#2f2f2f);border-left:0}

/* panels */
.panel{position:absolute;left:110px;width:980px;background:var(--panel);border:1px solid var(--panel-border);border-radius:4px;box-shadow:0 1px 3px rgba(0,0,0,.08)}
.panel-hero{top:157px;height:451px}
.panel-main{top:621px;height:334px}
.hero-photo{position:absolute;left:9px;top:9px;width:960px;height:310px;background:linear-gradient(100deg,#3a3a3f 0%,#8c8580 35%,#c9c5c0 55%,#a8703f 85%,#c48a4d 100%)}
.features{position:absolute;left:18px;top:335px;display:flex;gap:17px}
.feature{width:223px;height:99px;background:var(--charcoal);border-radius:3px;box-shadow:2px 2px 0 #1c1c1c;display:flex;padding:17px 0 0 13px;gap:13px;color:#fff}
.feature .icon{width:47px;height:47px;border-radius:50%;background:#fff;flex:none;display:flex;align-items:center;justify-content:center}
.feature h3{font-family:"Yanone Kaffeesatz",sans-serif;font-weight:700;font-size:25px;line-height:1;margin-top:-2px;letter-spacing:-.2px;text-transform:uppercase}
.feature p{font-size:11.5px;line-height:14.5px;margin-top:6px;width:120px;color:#eee}

.welcome{position:absolute;left:20px;top:18px;width:600px}
.section-title{font-family:"Yanone Kaffeesatz",sans-serif;font-weight:400;font-size:27px;display:flex;align-items:center;gap:10px;color:var(--heading-olive)}
.welcome p{font-size:12.5px;line-height:18px;margin-top:18px;color:var(--text)}
.welcome p:first-of-type{margin-top:11px}
.btn{display:inline-block;margin-top:18px;background:linear-gradient(#555,#2b2b2b);color:#fff;font-size:10px;padding:5px 7px 6px;border-radius:2px}
.testimonials{position:absolute;left:652px;top:18px}
.testimonials .section-title{color:#333}
.testimonial-box{margin-top:13px;width:306px;height:253px;background:linear-gradient(var(--olive-light),var(--olive));border:1px solid var(--olive-dark);border-radius:2px;padding:15px 0 0 12px}
.quote{display:flex;gap:16px;height:81px}
.avatar{width:63px;height:60px;border:3px solid #fff;border-radius:3px;background:linear-gradient(#d9d6d0,#9a948c);flex:none;box-shadow:0 1px 2px rgba(0,0,0,.3)}
.quote div{color:#fff;font-size:11px;line-height:15px}
.quote .date{font-size:12px}
.quote .text{font-weight:500}
.quote cite{font-style:italic;font-weight:500}

.footer-nav{position:absolute;left:109px;top:977px;font-size:11px;color:#444}
.footer-nav span{margin:0 7px}
.copyright{position:absolute;right:110px;top:977px;font-size:11px;color:#444}
</style>
</head>
<body>
<header>
  <div class="brand"><span class="brand-mark"></span>BRAMLEX</div>
  <div class="call">Call us today! <strong>125-480-7316</strong></div>
  <div class="social"><span class="s1"></span><span class="s2"></span></div>
  <a class="news" href="#">Get News &amp; Updates</a>
  <form class="search"><input type="text" placeholder="Enter your search"><button type="button">Submit</button></form>
  <nav class="nav"><a class="current" href="#">Home</a><a href="#">About Us</a><a href="#">Properties</a></nav>
</header>

<section class="panel panel-hero">
  <div class="hero-photo" role="img" aria-label="Hands signing a contract beside a model house with a sale tag"></div>
  <div class="features">
    <div class="feature">
      <div class="icon"><svg width="26" height="32" viewBox="0 0 26 32"><text x="13" y="27" text-anchor="middle" font-family="Ubuntu,sans-serif" font-weight="700" font-size="30" fill="#222">$</text></svg></div>
      <div><h3>For Investors</h3><p>Le Lorem Ipsum est simplement du faux texte.</p></div>
    </div>
    <div class="feature">
      <div class="icon"><svg width="28" height="24" viewBox="0 0 28 24"><path d="M1 3h5l3 12h14l3-9H8" fill="none" stroke="#222" stroke-width="2.5"/><path d="M8 6h18l-3 9H10z" fill="#222"/><circle cx="11" cy="20" r="2.5" fill="#222"/><circle cx="21" cy="20" r="2.5" fill="#222"/><rect x="15.5" y="7" width="2" height="5" fill="#fff"/></svg></div>
      <div><h3>For Buyers</h3><p>Le Lorem Ipsum est simplement du faux texte.</p></div>
    </div>
    <div class="feature">
      <div class="icon"><svg width="26" height="28" viewBox="0 0 26 28"><rect x="2" y="2" width="22" height="16" fill="#222"/><text x="13" y="9" text-anchor="middle" font-family="Ubuntu,sans-serif" font-size="6.5" fill="#fff">For</text><text x="13" y="16" text-anchor="middle" font-family="Ubuntu,sans-serif" font-size="6.5" fill="#fff">Sale</text><path d="M13 18v8M9 27l4-4 4 4" stroke="#222" stroke-width="1.5" fill="none"/></svg></div>
      <div><h3>For Sellers</h3><p>Le Lorem Ipsum est simplement du faux texte.</p></div>
    </div>
    <div class="feature">
      <div class="icon"><svg width="30" height="26" viewBox="0 0 30 26"><path d="M15 1L1 13h4v12h7v-8h6v8h7V13h4z" fill="#222"/></svg></div>
      <div><h3>For Homeowners</h3><p>Le Lorem Ipsum est simplement du faux texte.</p></div>
    </div>
  </div>
</section>

<main class="panel panel-main">
  <article class="welcome">
    <h2 class="section-title"><svg width="17" height="22" viewBox="0 0 17 22"><path d="M8.5 0a8.5 8.5 0 0 0-8.5 8.5C0 15 8.5 22 8.5 22S17 15 17 8.5A8.5 8.5 0 0 0 8.5 0z" fill="#6c6820"/><circle cx="8.5" cy="8.5" r="3.2" fill="#fff"/></svg>Welcome to Bramlex</h2>
    <p>Pusieurs variations de Lorem Ipsum peuvent être trouvées ici ou là, mais la majeure partie d'entre elles a été altérée par l'addition d'humour ou de mots aléatoires qui ne ressemblent pas une seconde à du texte standard.</p>
    <p>Si vous voulez utiliser un passage du Lorem Ipsum, vous devez être sûr qu'il n'y a rien d'embarrassant caché dans le texte. Tous les générateurs de Lorem Ipsum sur Internet tendent à reproduire le même extrait sans fin, ce qui fait de lipsum.</p>
    <p>Com le seul vrai générateur de Lorem Ipsum. Iil utilise un dictionnaire de plus de 200 mots latins, en combinaison de plusieurs structures de phrases, pour générer un Lorem Ipsum irréprochable. Le Lorem Ipsum ainsi obtenu ne contient aucune répétition,Le Lorem Ipsum ainsi obtenu ne contient aucune répétition.</p>
    <a class="btn" href="#">Read More</a>
  </article>
  <aside class="testimonials">
    <h2 class="section-title"><svg width="20" height="16" viewBox="0 0 20 16"><circle cx="6" cy="4" r="3.5" fill="#444"/><path d="M0 14c0-4 3-6 6-6s6 2 6 6z" fill="#444"/><circle cx="14" cy="6" r="3" fill="#444"/><path d="M9 16c0-3.5 2.5-5.5 5-5.5s5 2 5 5.5z" fill="#444"/></svg>Client Testimonials</h2>
    <div class="testimonial-box">
      <div class="quote"><div class="avatar" role="img" aria-label="Client portrait"></div><div><span class="date">14-12-2012</span><br><span class="text">On sait depuis longtemps que travailler avec du texte lisible etcon</span><br><cite>Dorian Pell</cite></div></div>
      <div class="quote"><div class="avatar" role="img" aria-label="Client portrait"></div><div><span class="date">14-12-2012</span><br><span class="text">On sait depuis longtemps que travailler avec du texte lisible etcon</span><br><cite>Dorian Pell</cite></div></div>
      <div class="quote"><div class="avatar" role="img" aria-label="Client portrait"></div><div><span class="date">14-12-2012</span><br><span class="text">On sait depuis longtemps que travailler avec du texte lisible etcon</span><br><cite>Dorian Pell</cite></div></div>
    </div>
  </aside>
</main>

<footer>
  <nav class="footer-nav"><a href="#">Home</a><span>|</span><a href="#">About Us</a><span>|</span><a href="#">Properties</a></nav>
  <p class="copyright">© Copyrights 2012 All rights Reserved</p>
</footer>
</body>
</html>
```